Motive für Servietten - Länderservietten - Deutschland, Italien, Frankreich, Spanien und Griechenland
Zielgruppe
Wir sind Versandhändler aus dem Bereich Büro Basteln Schule und Geschenkartikel und verkaufen neben Handelsware aus diesem Bereich auch viele eigene selbst gestaltete Artikel unter unserem Firmennamen morvako.
Aufgabenstellung
Gestaltet werden soll eine neue Motivserie für unsere Servietten
Thema sind hier Länderservietten
Passend für Feierlichkeiten die unter dem jeweiligen Land als Motto stehen oder auch für Veranstaltungen wie z.B. Fussball EM / WM
Basis sollte die Länderflaggen sein
Folgende Länder sollten im einheitlichen Designstil umgesetzt werden
Deutschland
Italien
Spanien
Frankreich
Griechenland
Rahmendaten zur Serviette
Größe: 30x30
Packung mit 20 Stück
Beispielfoto anbei
Ablauf im Wettbewerb
In der Wettbewerbsphase: Design des Motivs für die 5 Länder
Nach Abschluss des Wettbewerbs und Zuteilung des Gewinners:
-Erstellung der finalen Druckdateien (Beispiel Druckdatei anbei)
- Produktfotos alle Ansichten (Mockups können zur Verfügung gestellt werden)

```html
<!DOCTYPE html>
<html lang="de">
<head>
<meta charset="utf-8">
<title>Länderservietten</title>
<link href="https://fonts.googleapis.com/css2?family=Fredoka:wght@500;700&display=swap" rel="stylesheet">
<style>
  :root {
    --bg: #ffffff;
    --napkin: #f5f2e7;
    --it-green: #5a9a2a;
    --it-white: #f8f5ee;
    --it-red: #c0233a;
    --fr-blue: #15366b;
    --fr-white: #f6f4ee;
    --fr-red: #e8432c;
    --es-red: #c52a3a;
    --es-yellow: #f2c240;
    --gr-blue: #2e77b8;
    --gr-white: #f4f6f8;
    --gr-text: #f39200;
    --de-black: #141414;
    --de-red: #a51f1f;
    --de-gold: #f0b81c;
    --de-text: #ffffff;
    --glow: rgba(255,255,255,.9);
  }
  html, body { margin: 0; padding: 0; overflow: hidden; }
  body {
    width: 1200px; height: 766px; background: var(--bg);
    position: relative; font-family: "Fredoka", sans-serif;
  }
  .napkin {
    position: absolute; width: 320px; height: 320px;
    background: var(--napkin);
    box-shadow: 0 6px 18px rgba(0,0,0,.12);
  }
  .napkin--italy   { left: 60px;  top: 30px; }
  .napkin--france  { left: 440px; top: 95px; }
  .napkin--spain   { left: 820px; top: 190px; }
  .napkin--greece  { left: 60px;  top: 400px; }
  .napkin--germany { left: 460px; top: 430px; }
  .flag {
    position: absolute; left: 34px; top: 34px; width: 252px; height: 252px;
    -webkit-mask-image: radial-gradient(ellipse 72% 72% at 50% 50%, #000 62%, transparent 100%);
    mask-image: radial-gradient(ellipse 72% 72% at 50% 50%, #000 62%, transparent 100%);
  }
  .flag--italy { background: linear-gradient(90deg, var(--it-green) 0 30%, var(--it-white) 45% 55%, var(--it-red) 70% 100%); }
  .flag--france { background: linear-gradient(90deg, var(--fr-blue) 0 30%, var(--fr-white) 45% 55%, var(--fr-red) 70% 100%); }
  .flag--spain { background: linear-gradient(180deg, var(--es-red) 0 18%, var(--es-yellow) 40% 60%, var(--es-red) 82% 100%); }
  .flag--greece {
    background:
      linear-gradient(var(--gr-white), var(--gr-white)) 56px 0 / 28px 140px no-repeat,
      linear-gradient(var(--gr-white), var(--gr-white)) 0 56px / 140px 28px no-repeat,
      linear-gradient(var(--gr-blue), var(--gr-blue)) 0 0 / 140px 140px no-repeat,
      repeating-linear-gradient(180deg, var(--gr-blue) 0 28px, var(--gr-white) 28px 56px);
  }
  .flag--germany { background: linear-gradient(180deg, var(--de-black) 0 20%, var(--de-red) 40% 60%, var(--de-gold) 80% 100%); }
  .names {
    position: absolute; inset: 0; margin: 0; padding: 0; list-style: none;
    display: flex; flex-direction: column; align-items: center; justify-content: center;
    line-height: 1.05; font-weight: 500; font-size: 20px; letter-spacing: .5px;
    text-shadow: 0 0 4px var(--glow), 0 0 8px var(--glow);
  }
  .names .main { font-weight: 700; font-size: 28px; }
  .names--italy { color: var(--it-red); }
  .names--france { color: var(--fr-blue); font-weight: 700; font-size: 24px; }
  .names--spain { color: var(--es-red); }
  .names--greece { color: var(--gr-text); font-weight: 700; font-size: 23px; }
  .names--germany { color: var(--de-text); font-weight: 700; font-size: 21px; text-shadow: 0 0 6px rgba(255,255,255,.6); }
</style>
</head>
<body>
  <section class="napkin napkin--italy">
    <div class="flag flag--italy" role="img" aria-label="Brush-painted Italian flag with line drawings of pasta, pizza, scooter, olives and the Leaning Tower"></div>
    <ul class="names names--italy">
      <li>Italy</li><li class="main">Italia</li><li>Italien</li><li class="main">Italia</li><li>Italie</li>
    </ul>
  </section>

  <section class="napkin napkin--france">
    <div class="flag flag--france" role="img" aria-label="Brush-painted French flag with line drawings of the Eiffel Tower, baguettes, croissants and wine"></div>
    <ul class="names names--france">
      <li>France</li><li>Francia</li><li>Frankreich</li><li>Gallía</li>
    </ul>
  </section>

  <section class="napkin napkin--spain">
    <div class="flag flag--spain" role="img" aria-label="Brush-painted Spanish flag with line drawings of a guitar, grapes, dancer, barrel and bull"></div>
    <ul class="names names--spain">
      <li>Spain</li><li class="main">España</li><li>Spanien</li><li class="main">Spagna</li><li>Ispania</li>
    </ul>
  </section>

  <section class="napkin napkin--greece">
    <div class="flag flag--greece" role="img" aria-label="Brush-painted Greek flag with line drawings of a temple, columns, amphora and olives"></div>
    <ul class="names names--greece">
      <li>Greece</li><li>Grecia</li><li>Griechenland</li><li>Grèce</li><li>Hellas</li>
    </ul>
  </section>

  <section class="napkin napkin--germany">
    <div class="flag flag--germany" role="img" aria-label="Brush-painted German flag with line drawings of beer, pretzel, sausage, cathedral and gate"></div>
    <ul class="names names--germany">
      <li>Germany</li><li>Alemania</li><li>Deutschland</li><li>Germania</li><li>Allemagne</li>
    </ul>
  </section>
</body>
</html>
```